Re design and optimization of a website for pension Ora Vahi, a b&b in Tahiti, French Polynesia.

We have a website already : www.pensionoravahi.example

The general idea is to create a new site that is colorful, young and with an exotic, tropical feel since we are on a beautiful island.

The website will be in three languages, all the text is already available on our website, nothing changes.

All pages must have the name of the website (pension ora vahi b&b) our address, mail and phone number
It would be nice to have a link to our mail from every page

Sections have to be easy to update : text and pics

The sections needed are :

- Home page (accueil)

- Prices (tarifs)

- Bookings (reservations) = link to our mailbox : pensionoravahi@post.example )

- Pictures : in three separate categories that will pop up on this page : 1/ pics of the b&b 2/ pics of the surroundings 3/ customer's pics (we'll give new pics, not the current ones)

- Map of Tahiti : we'd like one map that we'll give you and also a Google map with our location, date and local time would be great

- Links (liens)

We let you see what would look best for the top banner and the switches, matching the logo and the pictures, make it nice and tropical !!
We have a few layouts that we did, maybe you will have a better idea of what we want by looking at them, if you can use them and have a good overall feel

We'd like to remind you guys that Tahiti is a dream destination, so you have to come up with something that the visitors will go : wow !!

We cater for backpackers to mid range accommodations and families, it all about a relaxed friendly atmosphere here !

NOTE THAT WE DON'T KNOW MUCH ABOUT PROGRAMMING AND CODING SO IT AS TO BE READY TO GO ON-LINE, ALL YOUR HELP IS APPRECIATED !!!
Also in Tahiti, the
INTERNET is quite low bandwidth so optimization is a must !

P.S : Live demo of the homepage is welcome ;)

We are available to all you for extra infos, good luck

regards,

remy & Pension Ora Vahi

Target Market(s)

Families and couples : individual rooms

Backpackers : Dormitories

people looking for an authentic stay in a familial environment

Customers of all ages and all nationalities

Requirements
Must have
• You must insist on the main page about :
the easy beach access
the breakfast included (with French baguette !)
Airport pick up 24/7
Many activities departing from our place : scuba diving, canyoning, 4x4 tour, rental cars, surf school, para-glide....

Please find a great way to highlight these !

```html
<!DOCTYPE html>
<html lang="en">
<head>
<meta charset="utf-8">
<title>Pension Ora Vahi – Prices</title>
<link href="https://fonts.googleapis.com/css2?family=Ubuntu:wght@400;500&family=Arimo:wght@400;700&family=Tinos:wght@400;700&display=swap" rel="stylesheet">
<style>
:root{
  --yellow:#f4f40c;
  --nav:#e8740c;
  --heading:#6e9128;
  --ink:#333333;
  --muted:#555555;
  --blue:#2d6cb2;
  --green:#1b8a1b;
  --panel:rgba(255,255,255,0.82);
  --rule:#3a3a3a;
  --brand:#c2281a;
}
*{box-sizing:border-box;margin:0;padding:0}
html,body{width:982px;height:1200px;overflow:hidden}
body{position:relative;font-family:"Arimo",Arial,sans-serif;color:var(--ink);}
.backdrop{position:absolute;inset:0;
  background:
    linear-gradient(90deg,rgba(20,90,60,.55) 0%,rgba(0,0,0,0) 14%,rgba(0,0,0,0) 86%,rgba(30,80,40,.6) 100%),
    linear-gradient(180deg,#4f9fe2 0%,#8cc6ee 30%,#2aa3b4 58%,#157d8c 78%,#c9b88a 100%);}
.site{position:absolute;left:110px;top:29px;width:765px;height:1139px}
.masthead{position:absolute;left:0;top:0;width:765px;height:138px;background:var(--yellow)}
.contact-phone{position:absolute;left:436px;top:46px;font-weight:700;font-size:22px;color:#111;white-space:nowrap}
.contact-phone small{position:absolute;right:0;top:-14px;font-size:11px;font-weight:700}
.brand{position:absolute;left:570px;top:8px;width:190px;height:120px;display:flex;align-items:center;gap:6px}
.brand-dot{width:20px;height:20px;border-radius:50%;background:var(--nav);flex:none}
.brand-name{font-family:"Ubuntu",sans-serif;font-weight:500;font-size:16px;color:var(--brand);white-space:nowrap}
.main-nav{position:absolute;left:8px;top:120px;display:flex;font-family:"Ubuntu",sans-serif;font-size:11px;font-weight:500}
.main-nav a{color:var(--nav);text-decoration:none;padding:0 8px;border-left:1px solid #d9c400}
.main-nav a:first-child{border-left:none;padding-left:0}
.hero{position:absolute;left:0;top:138px;width:765px;height:345px;
  background:linear-gradient(180deg,#1f4f8f 0%,#5f8fc2 22%,#3f7a4a 45%,#c34a3a 55%,#e9e6e0 62%,#2a5f86 75%,#173f66 100%)}
.content{position:absolute;left:0;top:483px;width:765px;height:598px;background:var(--panel)}
h2{font-family:"Ubuntu",sans-serif;font-weight:400;color:var(--heading);font-size:20px;letter-spacing:.5px}
.pricing{position:absolute;left:20px;top:24px;width:480px}
.intro{font-size:10.5px;line-height:14px;margin-top:3px;width:472px}
.rates{position:absolute;left:20px;top:103px;width:480px;border-collapse:collapse;background:#fff;font-size:9px;text-align:center}
.rates td{border:1px solid var(--rule);vertical-align:middle;padding:2px}
.rates .hdr{color:var(--blue);font-weight:700;font-size:10px}
.rates .hdr small{display:block;color:#222;font-size:8px;font-weight:400}
.rates .lead{font-weight:700;color:#111;font-size:10px}
.rates .lead small{display:block;font-weight:400;font-size:8px}
.num{font-family:"Tinos",serif;font-weight:700;color:var(--green);font-size:11px;line-height:20px}
.num b{display:inline-block;min-width:38px}
.num span{display:inline-block;min-width:30px;color:#222}
.rate-labels{font-family:"Tinos",serif;font-weight:700;font-size:11px;color:#111;text-align:left;line-height:20px;padding-left:10px!important}
.notes{position:absolute;left:20px;top:395px;font-size:10.5px;line-height:23px}
.payments{position:absolute;left:20px;top:454px}
.payments p{font-size:10.5px;margin-top:2px}
.cards{display:flex;gap:5px;margin-top:8px}
.card-box{width:36px;height:26px;border:1px solid #aaa;background:#fff}
.card-box:nth-child(2){background:#f4d7b0}
.card-box:nth-child(3){background:#dfe8f4}
.aside{position:absolute;left:527px;top:34px;width:230px;font-size:10px;line-height:13px;color:var(--muted)}
.lang{width:124px;height:18px;border:1px solid #bbb;background:#fff;font-size:10px;color:#666;padding:2px 6px;display:flex;justify-content:space-between}
.aside h2{margin-top:12px}
.info-card{margin-top:10px;padding-left:14px;font-family:"Tinos",serif;font-size:10px;line-height:13px;color:#111}
.info-card .name{display:flex;align-items:center;gap:6px;font-weight:700;font-size:14px;margin-bottom:3px}
.info-card .name i{width:14px;height:14px;border-radius:50%;background:#e6b92a;display:block}
.aside p{margin-top:12px}
.aside strong{color:#222}
.footer{position:absolute;left:0;top:1081px;width:765px;height:58px;background:var(--yellow);font-size:9.5px}
.social{position:absolute;left:16px;top:17px;display:flex;gap:6px}
.social span{width:24px;height:24px;border-radius:5px;display:block}
.social span:nth-child(1){background:#ef7d12}
.social span:nth-child(2){background:#3b5ba0}
.social span:nth-child(3){background:#3fa9e0}
.copyright{position:absolute;left:244px;top:24px;color:#333}
.footer-links{position:absolute;right:18px;top:24px;display:flex;gap:14px}
.footer-links a{color:#333}
</style>
</head>
<body>
<div class="backdrop" role="img" aria-label="Tropical beach with palm trees and lagoon"></div>
<div class="site">
  <header class="masthead">
    <div class="contact-phone"><small>tahiti</small>Tel: 50 12 34</div>
    <div class="brand"><span class="brand-dot"></span><span class="brand-name">Pension Ora Vahi</span></div>
    <nav class="main-nav">
      <a href="#">HOME</a><a href="#">PRICES</a><a href="#">BOOKING</a><a href="#">GALLERY</a><a href="#">MAP OF TAHITI</a><a href="#">LINKS</a>
    </nav>
  </header>
  <div class="hero" role="img" aria-label="Harbour with sailing boats, red-roofed town and green hills"></div>

  <main class="content">
    <section class="pricing">
      <h2>PRICING</h2>
      <p class="intro">We have individual or familial Rooms - Dormitory.  In addition, breakfast (buffet) is included every morning with your stay with us. Airport transfer is provide 24 hr a day for a fee.</p>
    </section>

    <table class="rates">
      <colgroup><col style="width:91px"><col style="width:88px"><col style="width:107px"><col style="width:111px"><col style="width:83px"></colgroup>
      <tr style="height:42px">
        <td class="lead">1euro = 120 FCP<small>RATE per bedroom (single or double)</small></td>
        <td class="hdr">LARGE BEDROOM<small>1 à 5 Pax</small></td>
        <td class="hdr">REGULAR BEDROOM<small>1 à 3 Pax</small></td>
        <td class="hdr">SINGLE ROOM<small>1 à 2 Pax</small></td>
        <td class="hdr">DORMS BED<small>per person</small></td>
      </tr>
      <tr style="height:91px">
        <td class="rate-labels">RATE :<br>- Night<br>-Week<br>(per night)</td>
        <td class="num"><b>FCP</b><span>Euros</span><br><b>7 500</b><span>62,9</span><br><b>7 500</b><span>58,7</span></td>
        <td class="num"><b>FCP</b><span>Euros</span><br><b>7 000</b><span>58,7</span><br><b>6 500</b><span>54,5</span></td>
        <td class="num"><b>en FCP</b><span>Euros</span><br><b>6 500</b><span>54,5</span><br><b>6 000</b><span>50,3</span></td>
        <td class="num"><b>en FCP</b><span>Euros</span><br><b>2 500</b><span>21</span><br><b>2 300</b><span>19,3</span></td>
      </tr>
      <tr style="height:52px">
        <td class="hdr">SUPLEMENTARY BED<small>in the rooms</small></td>
        <td class="hdr">Transfer<br>per person<small>airport or ferry/pension</small></td>
        <td class="hdr">PHONE<br>per minute</td>
        <td class="hdr">INTERNET</td>
        <td class="hdr">WASHING MACHINE<small>the basket of 5 kgs</small></td>
      </tr>
      <tr style="height:94px">
        <td class="num"><b>en FCP</b><span>Euros</span><br><b>2 500</b><span>21</span><br><b>2 300</b><span>19,3</span></td>
        <td class="num"><b>en FCP</b><span>Euros</span><br><b>1500</b><span>12,6</span><br><span style="min-width:0">24/24</span></td>
        <td class="num"><b>en FCP</b><span>Euros</span><br><b>tahiti 100</b><span>0,9</span><br><b>islands 200</b><span>1,7</span><br><b>exterieur 300</b><span>2,5</span></td>
        <td class="num"><b>en FCP</b><span>Euros</span><br><b>½ hr 500</b><span>4,2</span><br><b>hour 1000</b><span>8,4</span></td>
        <td class="num"><b>en FCP</b><span>Euros</span><br><b>800</b><span>6,7</span></td>
      </tr>
    </table>

    <div class="notes">
      <p>TARIFS 2008 (tax included)</p>
      <p>We provide free luggage storage upon condition that you return to stay another night.</p>
    </div>

    <section class="payments">
      <h2>PAYMENTS</h2>
      <p>CREDIT CARD ACCEPTED : CORALPAY - LAGOONCARD - TRAVELERS CHEQUE - CASH</p>
      <div class="cards"><span class="card-box"></span><span class="card-box"></span><span class="card-box"></span></div>
    </section>

    <aside class="aside">
      <div class="lang"><span>Select Language</span><span>▾</span></div>
      <h2>INFORMATION</h2>
      <div class="info-card">
        <div class="name"><i></i>Pension Ora Vahi</div>
        BP 204410 Paea 98711<br>Tiare Nui Tahiti- French Polynesia<br>Telephone: 50 12 34 87 65 43
      </div>
      <h2>RESERVATIONS</h2>
      <p><strong>For all reservations we ask : 30% deposit</strong></p>
      <p><strong>By post (personal check in euro) adress to :</strong></p>
      <p>Mr TAERO Manu<br>Pension Ora Vahi BP 204410 Paea 98711<br>Tiare Nui<br>TAHITI - French Polynesia</p>
      <p><strong>Via e mail :</strong> pensionoravahi@post.example<br>Send credit card (number/name/exp date)</p>
      <p>For increased security we advise you to send this information in two separate e mails In case of cancellation, deposit forfeited</p>
      <p>Please ensure you include correct details of full name; check in/out dates, accomodation type</p>
    </aside>
  </main>

  <footer class="footer">
    <div class="social"><span></span><span></span><span></span></div>
    <div class="copyright">Copyright © 2011. All Rights Reserved.</div>
    <div class="footer-links"><a href="#">About Us</a><a href="#">Contact Us</a><a href="#">Terms Of Service</a></div>
  </footer>
</div>
</body>
</html>
```